Fernbrook Vale Executive Development Workshop Series

* Had error in first version of MS Word doc and have re-uploaded - twelve subject areas, not nine *
I'd like a flyer to print to hand out and post on my website fernbrookvale.com to advertise a workshop series I'm launching. I'd like it to build strongly on the wonderful logo you did and Scottish theme...and to have the same "feel" as my website. fernbrookvale.com
It should be 8.5x11, single sided. Not sure if I should use full color glossy or two-color on nice paper. Regardless, I will most likely have it done on a color copier and will not put it on a printing press.
I have typed up a document with all the information in a MS Word file, but need you to lay it out in an aesthetically pleasing way. I have attached that MS Word file.
I am also attaching a handful of similar flyer documents from other non-competing coaches in my network. I think they all have their merits, but leave me under-whelmed.
I'm also attaching a picture of me and some pictures of Scotland my parents took about 10 years ago. I'm reluctantly open to stock photos, just not too obvious or hackneyed (if that word can be applied to pictures as well as expressions).
Lastly, this workshop series will be an ongoing thing, so I'd like to be able to make minor edits myself with things like new dates or topics.
Thank you!
Target Market(s)
Small business owners and emerging leaders with large companies
Colors
Designer to choose colors to be used in the design.
Requirements
Should not have
- Obviously stock photos

```html
<!DOCTYPE html>
<html lang="en">
<head>
<meta charset="utf-8">
<title>Fernbrook Vale Executive Development Workshop Series</title>
<link rel="stylesheet" href="https://fonts.googleapis.com/css2?family=Roboto:wght@300;400;500;700&family=Open+Sans:wght@400;600&family=Dancing+Script:wght@600&display=swap">
<style>
  :root {
    --forest: #354f10;
    --forest-text: #3d5914;
    --sage: #d3e1b5;
    --mist: #eff0f2;
    --ink: #222;
    --white: #fff;
    --rule: #d9dcd4;
    --member-mark: #d8d8d8;
  }
  * { box-sizing: border-box; margin: 0; padding: 0; }
  html, body { width: 975px; height: 1200px; overflow: hidden; background: var(--white); }
  body { position: relative; font-family: "Roboto", Arial, sans-serif; color: var(--ink); }

  .sage-strip { position: absolute; left: 618px; width: 357px; background: var(--sage); }
  .sage-strip--top { top: 0; height: 61px; }
  .sage-strip--bottom { top: 1143px; height: 57px; }

  .brand { position: absolute; left: 0; top: 0; width: 534px; height: 182px; }
  .brand__name {
    position: absolute; left: 60px; top: 52px;
    font-family: "Roboto", Arial, sans-serif; font-weight: 500; font-size: 46px;
    color: var(--forest-text); letter-spacing: 1px;
    display: flex; align-items: center; gap: 14px;
  }
  .brand__dot { width: 20px; height: 20px; border-radius: 50%; background: var(--forest-text); }
  .brand__tag {
    position: absolute; left: 200px; top: 118px; width: 160px;
    border-top: 1px solid #b7c99a; padding-top: 4px;
    font-size: 10px; letter-spacing: 2px; text-align: center; color: var(--forest-text);
  }
  .member-mark {
    position: absolute; left: 452px; top: 92px; width: 44px; height: 44px;
    background: var(--member-mark);
  }

  .hero-photo {
    position: absolute; left: 0; top: 182px; width: 534px; height: 361px;
    background: linear-gradient(180deg, #b7c0c8 0%, #9aa37e 22%, #7f8f52 45%, #a4703a 70%, #6e7d3c 100%);
  }
  .coach-portrait {
    position: absolute; left: 408px; top: 414px; width: 106px; height: 122px;
    border: 3px solid var(--sage); background: linear-gradient(180deg, #6d6c78, #8d7f72);
  }

  .intro {
    position: absolute; left: 0; top: 543px; width: 534px; height: 103px;
    background: var(--sage); padding: 8px 17px 0 26px;
    font-size: 12.5px; font-weight: 500; line-height: 18px; text-align: justify;
  }
  .trust {
    position: absolute; left: 0; top: 646px; width: 534px; height: 96px;
    background: var(--mist); padding: 9px 20px 0 29px;
    font-size: 13px; font-weight: 700; color: #333; line-height: 19.5px; text-align: justify;
  }
  .topics-lead {
    position: absolute; left: 0; top: 742px; width: 534px; height: 46px;
    background: var(--forest); color: var(--white); padding: 6px 18px 0 30px;
    font-size: 12px; font-weight: 500; line-height: 17px;
  }
  .topics {
    position: absolute; left: 0; top: 790px; width: 534px; table-layout: fixed;
    border-collapse: collapse; font-family: "Open Sans", Arial, sans-serif; font-size: 11.3px; line-height: 15px;
  }
  .topics col.topics__date-col { width: 100px; }
  .topics td { border-bottom: 1px solid var(--rule); padding: 3px 0 3px; vertical-align: top; }
  .topics td.topics__date { padding-left: 30px; color: #333; white-space: nowrap; font-size: 10.5px; }
  .topics td.topics__desc { padding-right: 26px; color: #333; }
  .topics__title { font-weight: 600; color: var(--forest-text); }
  .topics tr:last-child td { border-bottom: none; }

  .series-panel {
    position: absolute; left: 540px; top: 61px; width: 435px; height: 1082px;
    background: var(--forest); color: var(--white); text-align: center;
  }
  .series-panel__brand { margin-top: 33px; font-size: 38px; line-height: 44px; }
  .series-panel__title { margin-top: 4px; font-size: 50px; font-weight: 700; line-height: 58px; text-shadow: 0 2px 3px rgba(0,0,0,.35); }
  .series-panel__when { margin-top: 6px; font-size: 40px; line-height: 46px; }
  .register__script { margin-top: 34px; font-family: "Dancing Script", cursive; font-size: 44px; line-height: 50px; }
  .register__url { margin-top: 6px; font-size: 21px; font-weight: 700; line-height: 28px; }
  .register__hint { font-size: 12.5px; font-weight: 500; line-height: 18px; }
  .includes__head { margin-top: 40px; font-size: 23px; font-weight: 400; line-height: 25px; }
  .includes__item { margin: 14px auto 0; width: 345px; font-size: 14px; font-weight: 300; line-height: 19px; color: #e4ead8; }
  .includes__item strong { color: var(--white); font-size: 15px; font-weight: 700; }
  .venue {
    margin: 24px auto 0; width: 362px; height: 137px; background: var(--sage); color: #111;
    padding-top: 12px; box-shadow: 0 2px 4px rgba(0,0,0,.35);
  }
  .venue__head { font-size: 20px; font-weight: 700; line-height: 24px; }
  .venue__body { font-size: 16px; line-height: 21px; margin-top: 2px; }
  .venue__place { font-weight: 500; }
  .venue__addr { font-size: 16px; font-weight: 500; margin-top: 10px; }
  .coach__name { margin-top: 12px; font-family: "Open Sans", Arial, sans-serif; font-size: 29px; font-weight: 600; line-height: 34px; }
  .coach__role { font-size: 13.5px; line-height: 18px; color: #e4ead8; }
  .coach__contact { margin-top: 10px; font-size: 17px; line-height: 21px; }
  .coach__contact b { font-weight: 700; }
  .coach__note { margin: 14px auto 0; width: 360px; font-size: 14px; font-weight: 300; line-height: 18px; color: #e4ead8; }
</style>
</head>
<body>
  <div class="sage-strip sage-strip--top"></div>
  <div class="sage-strip sage-strip--bottom"></div>

  <header class="brand">
    <div class="brand__name"><span class="brand__dot"></span>Fernbrook Vale</div>
    <div class="brand__tag">BUSINESS COACHING</div>
    <div class="member-mark" role="img" aria-label="Coaching alliance membership mark"></div>
  </header>

  <div class="hero-photo" role="img" aria-label="Scottish village by a loch with highland cattle grazing in the foreground"></div>
  <div class="coach-portrait" role="img" aria-label="Portrait photo of the coach"></div>

  <p class="intro">A positive, fresh, results-driven approach for businesses to increase profits by building confidence, command and control in owners and executives. We will use proven leadership and business strategies to improve work-life balance, buy-in, and company value. Here's your opportunity to meet with other like-minded business owners and executives once a month in a private and confidential setting.</p>

  <p class="trust">Participation and trust is vital to your investment; no holding back. Due to the confidential nature of the intensive workshops, all participants will sign a confidentiality agreement. Additionally, we will only allow one company per industry to be represented.</p>

  <p class="topics-lead">We've got twelve subject areas planned, and while they are all powerful, we will shift from high-level strategy topics to “where the rubber meets the road” topics.</p>

  <table class="topics">
    <colgroup><col class="topics__date-col"><col></colgroup>
    <tr><td class="topics__date">Sep 7-</td><td class="topics__desc"><span class="topics__title">My Company Owns Me</span>- What a CEO should and should not do</td></tr>
    <tr><td class="topics__date">Oct 5-</td><td class="topics__desc"><span class="topics__title">Taking Vision / Mission / Values Down</span> To The Molecular Level Of Your Company</td></tr>
    <tr><td class="topics__date">Nov 2-</td><td class="topics__desc"><span class="topics__title">People Problems</span>– The biggest waste of time and money for every small business</td></tr>
    <tr><td class="topics__date">Dec 7-</td><td class="topics__desc"><span class="topics__title">Value Delivery Systems</span>- Re-think everything you think you know about creating value</td></tr>
    <tr><td class="topics__date">Jan 4, 2018-</td><td class="topics__desc"><span class="topics__title">Rally Your Team Around A Goal</span>- How to create a meaningful company goal and rally the troops around it</td></tr>
    <tr><td class="topics__date">Feb 1-</td><td class="topics__desc"><span class="topics__title">Building Your Executive Leadership Team</span>- You can't succeed without one</td></tr>
    <tr><td class="topics__date">Mar 1-</td><td class="topics__desc"><span class="topics__title">Improve Your Outside Sales Efforts</span>-Help your sales force to be busy AND successful</td></tr>
    <tr><td class="topics__date">Apr 5-</td><td class="topics__desc"><span class="topics__title">Every Brain In The Game</span>- Engage your team and build a strong culture</td></tr>
    <tr><td class="topics__date">May 3-</td><td class="topics__desc"><span class="topics__title">Repeatable Processes</span>- Coach your employees how to get predictable results every time</td></tr>
    <tr><td class="topics__date">Jun 7 –</td><td class="topics__desc"><span class="topics__title">Finding and Filling Profit Holes</span>- Most small businesses waste more money than they profit</td></tr>
    <tr><td class="topics__date">*Jul 12 -</td><td class="topics__desc"><span class="topics__title">Put Your Payroll On A Diet</span>- Why waste happens, what to do about it and how it helps everyone</td></tr>
    <tr><td class="topics__date">Aug 2-</td><td class="topics__desc">Truly, How Effective Are You With This Whole “Leadership” Thing?</td></tr>
  </table>

  <aside class="series-panel">
    <p class="series-panel__brand">Fernbrook Vale</p>
    <h1 class="series-panel__title">EXECUTIVE<br>DEVELOPMENT<br>WORKSHOP<br>SERIES</h1>
    <p class="series-panel__when">FIRST THURSDAYS</p>

    <p class="register__script">To Register</p>
    <p class="register__url">Go to: fernbrookvale.com/exec-dev</p>
    <p class="register__hint">and click the registration link</p>

    <h2 class="includes__head">EACH MONTH OF THIS MONTHLY<br>WORKSHOP SERIES INCLUDES:</h2>
    <p class="includes__item"><strong>3-Hour Intensive Workshop -</strong> High-energy, creative sessions with engaging and relevant business topics, peer group advisory board (master mind), and networking (9am – 12pm, dates above)</p>
    <p class="includes__item"><strong>90-minute one-on-one coachingsession –</strong> to help you absorb and apply the revelations from the group sessions to your own business (mutually scheduled)</p>

    <div class="venue">
      <p class="venue__head">All monthly Intensive<br>Workshops will be</p>
      <p class="venue__body"><b>9am - 12pm</b> on the dates above at<br><span class="venue__place">Millrace Coworking</span> at</p>
      <p class="venue__addr">212 Foundry Lane, Millbrook. NC 27000</p>
    </div>

    <p class="coach__name">Alan Drummond,</p>
    <p class="coach__role">Certified Professional Business Coach</p>
    <p class="coach__contact">alan@fernbrookvale.com, 555-014-2286,<br><b>www.fernbrookvale.com</b></p>
    <p class="coach__note">All one-on-one coaching sessions will be mutually scheduled with Alan Drummond once you have registered</p>
  </aside>
</body>
</html>
```